VelloTek needs web site design

We need a web site design for our product called 'VelloTek'. We develop an asset management system that can manage all kind of assets. Currently we have a logo theme and would like to use similar color scheme; the content concept is pretty much in http://tdalwynne.net but the product was called "Kestel Suite" at the time and is now called "VelloTek". Vello means Vast Equipment Ledger Logging Organizer.
Please use generic image for asset (not just bridges) e.g buildings, trucks, powerlines. train, bus, lightrail etc..
Please emphazise on the data management and security, and distributed networking.

the new website address is https://www.vellotek.example/

name on business card

Thomas Dalwynne 555-014-7392
Principal Architect / Software Engineer

Tara Dalwynne 555-018-2641
Software Engineer

Coding

Coded - Design and coding required

Number of Pages Required

1 page

```html
<!DOCTYPE html>
<html lang="en">
<head>
<meta charset="utf-8">
<title>VelloTek</title>
<link rel="stylesheet" href="https://fonts.googleapis.com/css2?family=Open+Sans:wght@400;600&display=swap">
<style>
  :root {
    --bg: #ffffff;
    --body-text: #3f3f3f;
    --gold: #c9a14b;
    --on-gold: #ffffff;
  }
  * { margin: 0; padding: 0; box-sizing: border-box; }
  html, body {
    width: 1200px;
    height: 341px;
    overflow: hidden;
    background: var(--bg);
    font-family: "Open Sans", sans-serif;
  }
  .page { position: relative; width: 1200px; height: 341px; }

  .article-columns {
    position: absolute;
    top: 0;
    left: 0;
    width: 1200px;
    height: 94px;
    overflow: hidden;
  }
  .article-column {
    position: absolute;
    top: -5px;
    font-size: 13.6px;
    line-height: 19.2px;
    color: var(--body-text);
    white-space: nowrap;
  }
  .article-column span { display: block; }
  .col-one { left: 120px; }
  .col-two { left: 462px; }
  .col-three { left: 808px; }

  .site-footer {
    position: absolute;
    left: 120px;
    top: 158px;
    width: 958px;
    height: 147px;
    background: var(--gold);
    border-radius: 4px;
    color: var(--on-gold);
  }
  .brand {
    position: absolute;
    left: 26px;
    top: 25px;
    display: flex;
    align-items: center;
    gap: 10px;
  }
  .brand-square {
    width: 36px;
    height: 36px;
    border: 2.5px solid var(--on-gold);
  }
  .brand-name {
    font-size: 32px;
    font-weight: 600;
    line-height: 1;
    color: var(--on-gold);
  }
  .social-links {
    position: absolute;
    right: 24px;
    top: 30px;
    display: flex;
    gap: 6px;
  }
  .social-links a {
    display: block;
    width: 30px;
    height: 30px;
    border: 2px solid var(--on-gold);
    border-radius: 50%;
  }
  .footer-nav {
    position: absolute;
    left: 25px;
    top: 104px;
    display: flex;
    gap: 43px;
    list-style: none;
    font-size: 13.6px;
  }
  .footer-nav a { color: var(--on-gold); text-decoration: none; }
  .copyright {
    position: absolute;
    right: 23px;
    top: 105px;
    font-size: 12px;
  }
</style>
</head>
<body>
<div class="page">
  <section class="article-columns">
    <p class="article-column col-one">
      <span>page when looking at its layout. The point</span>
      <span>of using Lorem Ipsum is that it has a more-</span>
      <span>or-less normal distribution of letters, as</span>
      <span>opposed to using 'Content here, content</span>
      <span>here', making it look like readable English.</span>
    </p>
    <p class="article-column col-two">
      <span>default model text, and a search for 'lorem</span>
      <span>ipsum' will uncover many web sites still in</span>
      <span>their infancy. Various versions have evolved</span>
      <span>over the years, sometimes by accident, some-</span>
      <span>times on purpose (injected humour and the</span>
    </p>
    <p class="article-column col-three">
      <span>over the years, sometimes by accident, some-</span>
      <span>times on purpose (injected humour and the</span>
      <span>like).</span>
      <span>It is a long established fact that a reader will be</span>
      <span>distracted by the readable content of a page</span>
    </p>
  </section>

  <footer class="site-footer">
    <div class="brand">
      <div class="brand-square"></div>
      <span class="brand-name">VelloTek</span>
    </div>
    <div class="social-links">
      <a href="#" aria-label="Professional network"></a>
      <a href="#" aria-label="Social network"></a>
    </div>
    <ul class="footer-nav">
      <li><a href="#">Home</a></li>
      <li><a href="#">Portfolio</a></li>
      <li><a href="#">Download</a></li>
      <li><a href="#">About</a></li>
      <li><a href="#">Contact</a></li>
    </ul>
    <p class="copyright">Copyright © Dalwynne &amp; Associates 2009</p>
  </footer>
</div>
</body>
</html>
```